Metal head/ Sushi chef wanting artistic yet high imact business card

I'm sushi chef for make living in Australia originally from Tokyo Japan.
I'm also guitarist/composer as well on progressive metalcore/djent genre.
My favorite visual art is Mandala. Sacred geometries, Fractals, Paisleys are also things fit in me. I like dark color, earth color, and sometimes psychedelic patterns.
I want to hand out my business card when I meet new people in music industries or someone who is wanting private sushi chef for their party.
I know metal and sushi are far different subjects but they are all my passion. I would like to work with the designer who can create something cool from information above.

https://www.viewtrove.com/channel/QX7h4LpRzd2VnWe9kT3BFs8j
https://tunebarrel.com/user-817264093

Front
my name, Kenjiro Motsuba
occupation, "Sushi chef" "Metal guitarist/composer"
Email address, velmoquartz@mailorb.com
Phone number, (61)498271053

Back:
My Viewtrove channel, Pagefolk, Tunebarrel, Glintory. All of those are searchable by "Velmoquartz" The website mentioned above can be described as their logos.

Target Market(s)

people in Music industry, such as musicians, venue managers, promoters.
People who wants to have private sushi chef for their private function, party or events.

Industry/Entity Type

Artists

Contact Information for Business Card

Uploaded photos are just image reference. not thinking to use them.
My details:
I like :
energetic music that has a lot of details such as Progressive metalcore, jazz, djent, psychedelic music.
Spiritual thoughs, Buddism, fundamentals, relaxation music, 420, weed culture, Free thoughts
U.S street culture, skate board, kelps, surf, bicycle, nature, camping, hiking, ocean, mountain, desert, countryside,
permaculture, natural farming, organic farming, compost, self sufficient.
nigiri sushi, art sushi, something/someone beautiful in mind.

Dislike:
Fakes, Bullshits, format, negative, preservatives, artificial colors, illuminati, satanism, manipulation, mass favorites, big society, politics, Chinese letters on western design

Colors
0455a3
000000
7c7c7c
00a990
acd036
f37122

Requirements
Must have
• Front
• my name, Kenjiro Motsuba
• occupation, "Sushi chef" "Metal guitarist/composer"
• Email address, velmoquartz@mailorb.com
• Phone number, (61)498271053
• Back:
• My Viewtrove channel, Pagefolk, Tunebarrel, Glintory. All of those are searchable by "Velmoquartz" The website mentioned above can be described as their logos.
Nice to have
• something based on one of those either back ground or logo:
• Mandala, Sacred Geometry, Fractal art
Should not have
• pop essence. mass favorites, pink, Chinese letters, asian fonts, something asian

```html
<!DOCTYPE html>
<html lang="en">
<head>
<meta charset="utf-8">
<title>Kenjiro Motsuba — Business Card</title>
<link href="https://fonts.googleapis.com/css2?family=Cinzel:wght@400;700&family=Roboto:wght@400;500&display=swap" rel="stylesheet">
<style>
  :root {
    --bg: #2a2a2c;
    --card: #0b0b0c;
    --card-edge: #161618;
    --violet: #4238b8;
    --violet-deep: #2a2480;
    --green: #2fae4a;
    --green-light: #9bd23c;
    --cyan: #1fa6d8;
  }
  * { margin: 0; padding: 0; box-sizing: border-box; }
  html, body { width: 1200px; height: 1101px; overflow: hidden; }
  body {
    background: var(--bg);
    position: relative;
    font-family: "Roboto", Arial, sans-serif;
  }
  .card {
    position: absolute;
    left: 170px;
    width: 860px;
    height: 491px;
    background: radial-gradient(ellipse at 40% 40%, #19191b 0%, var(--card) 70%);
    border: 1px solid var(--card-edge);
    overflow: hidden;
    box-shadow: 0 14px 30px rgba(0,0,0,.55);
  }
  .card--back { top: 40px; }
  .card--front { top: 570px; }

  /* back */
  .back-mandala { position: absolute; left: 560px; top: -40px; width: 400px; height: 400px; }
  .contact-list { position: absolute; left: 62px; top: 150px; list-style: none; }
  .contact-item {
    display: flex; align-items: center; gap: 12px;
    color: var(--green); font-size: 21px; margin-bottom: 12px;
  }
  .contact-icon {
    width: 26px; height: 26px; border-radius: 50%;
    background: var(--violet);
    display: flex; align-items: center; justify-content: center;
  }
  .social-list {
    position: absolute; left: 78px; top: 290px;
    display: flex; gap: 18px; list-style: none;
  }
  .social-item {
    display: flex; align-items: center; gap: 6px;
    color: var(--green); font-size: 15px; font-weight: 500;
  }
  .social-dot { width: 14px; height: 14px; border-radius: 50%; background: var(--violet); }
  .handle {
    position: absolute; left: 100px; top: 326px;
    color: var(--green); font-size: 22px; font-weight: 500;
  }

  /* front */
  .front-art { position: absolute; left: 190px; top: 30px; width: 480px; height: 300px; }
  .name {
    position: absolute; left: 0; width: 100%; top: 268px; text-align: center;
    font-family: "Cinzel", Georgia, serif; font-weight: 700; font-size: 62px;
    background: linear-gradient(90deg, var(--green) 0%, var(--green-light) 55%, var(--green) 100%);
    -webkit-background-clip: text; background-clip: text; color: transparent;
    letter-spacing: 1px;
  }
  .roles {
    position: absolute; left: 0; width: 100%; top: 352px; text-align: center;
    font-family: "Cinzel", Georgia, serif; color: var(--violet); line-height: 1.3;
  }
  .role { display: block; font-size: 19px; }
</style>
</head>
<body>

<section class="card card--back" aria-label="Card back">
  <svg class="back-mandala" viewBox="0 0 400 400" role="img" aria-label="Mandala ornament in violet, green and cyan">
    <defs>
      <radialGradient id="mandalaBack">
        <stop offset="0" stop-color="#1fa6d8"/>
        <stop offset=".25" stop-color="#1c8a7a"/>
        <stop offset=".45" stop-color="#2fae4a"/>
        <stop offset=".62" stop-color="#2a2480"/>
        <stop offset="1" stop-color="#4238b8" stop-opacity=".55"/>
      </radialGradient>
    </defs>
    <circle cx="270" cy="200" r="200" fill="url(#mandalaBack)"/>
  </svg>

  <ul class="contact-list">
    <li class="contact-item">
      <span class="contact-icon">
        <svg width="14" height="14" viewBox="0 0 24 24"><path fill="#0b0b0c" d="M6.6 10.8a15 15 0 0 0 6.6 6.6l2.2-2.2a1 1 0 0 1 1-.25 11.4 11.4 0 0 0 3.6.57 1 1 0 0 1 1 1V20a1 1 0 0 1-1 1A17 17 0 0 1 3 4a1 1 0 0 1 1-1h3.5a1 1 0 0 1 1 1c0 1.25.2 2.45.57 3.57a1 1 0 0 1-.25 1z"/></svg>
      </span>
      (61)498271053
    </li>
    <li class="contact-item">
      <span class="contact-icon">
        <svg width="14" height="14" viewBox="0 0 24 24"><path fill="#0b0b0c" d="M3 5h18v14H3z"/><path fill="none" stroke="#4238b8" stroke-width="2" d="M3 6l9 7 9-7"/></svg>
      </span>
      velmoquartz@mailorb.com
    </li>
  </ul>

  <ul class="social-list">
    <li class="social-item"><span class="social-dot"></span>Pagefolk</li>
    <li class="social-item"><span class="social-dot"></span>Tunebarrel</li>
    <li class="social-item"><span class="social-dot"></span>Glintory</li>
    <li class="social-item"><span class="social-dot"></span>Viewtrove</li>
  </ul>
  <p class="handle">Velmoquartz</p>
</section>

<section class="card card--front" aria-label="Card front">
  <svg class="front-art" viewBox="0 0 480 300" role="img" aria-label="Illustrated chef holding chopsticks and a guitar in front of a half mandala">
    <defs>
      <radialGradient id="mandalaFront" cx="240" cy="300" r="240" gradientUnits="userSpaceOnUse">
        <stop offset="0" stop-color="#2fae4a"/>
        <stop offset=".5" stop-color="#1d6b3a"/>
        <stop offset=".62" stop-color="#2a2480"/>
        <stop offset="1" stop-color="#4238b8" stop-opacity=".6"/>
      </radialGradient>
      <linearGradient id="figureFill" x1="0" y1="0" x2="0" y2="1">
        <stop offset="0" stop-color="#5a4636"/>
        <stop offset=".45" stop-color="#e8c9a8"/>
        <stop offset="1" stop-color="#f2f2f2"/>
      </linearGradient>
    </defs>
    <path d="M0 300 A240 240 0 0 1 480 300 Z" fill="url(#mandalaFront)"/>
    <rect x="165" y="0" width="160" height="270" rx="60" fill="url(#figureFill)" opacity=".85"/>
  </svg>

  <h1 class="name">Kenjiro Motsuba</h1>
  <p class="roles">
    <span class="role">Sushi Chef</span>
    <span class="role">Metal Guitarist/Composer</span>
  </p>
</section>

</body>
</html>
```